Wine label design for my wife. Wine called "The Mirabel"

I need a wine label face lift of one of my premium wines in my collection. My wine sells in Harbor Lark's all over the States. My current label is called The Mirabel (my wife's name) and the illustration of her eyes is done by a well know artist from South Africa. I do not have to use this illustration and therefor I attached several pictures of her and her eyes, even when she was a little girl. The wine's also made in South Africa. This is a premium wine that we only sell 2000 bottles per year. The wine sells at 60 usd per bottle, The current label is too white. I also think her eyes should look more at the person buying it, than away from them.

Target Market(s)

Top end wine buyers

Font styles to use
Decorative
Script

Requirements
Must have
• 'The Mirabel' must be on the label
An illustration must be on the label
Basically all the info that's on the current label must be on by law. As per Sample
Nice to have
• Maybe some ideas of her whole face?
Should not have
• any gold colour

```html
<!DOCTYPE html>
<html lang="en">
<head>
<meta charset="utf-8">
<title>The Mirabel – Wine Label</title>
<link href="https://fonts.googleapis.com/css2?family=Tinos:wght@400;700&family=Yellowtail&family=Open+Sans&display=swap" rel="stylesheet">
<style>
  :root {
    --page: #ffffff;
    --label-ink: #28272d;
    --grape-light: #3a3941;
    --grape-dark: #2c2b32;
    --ornament: #3d3c45;
    --trim: #c3c4cc;
    --script: #ffffff;
    --caption: #1a1a1a;
  }
  html, body {
    margin: 0;
    padding: 0;
    width: 1200px;
    height: 848px;
    overflow: hidden;
    background: var(--page);
  }
  .canvas {
    position: relative;
    width: 1200px;
    height: 848px;
  }
  .label {
    position: absolute;
    left: 198px;
    top: 115px;
    width: 412px;
    height: 601px;
  }
  .label-shape {
    position: absolute;
    inset: 0;
  }
  .label-text {
    position: absolute;
    left: 0;
    width: 412px;
    text-align: center;
    margin: 0;
  }
  .house-name {
    top: 120px;
    font-family: "Tinos", serif;
    font-weight: 700;
    font-size: 17px;
    letter-spacing: 2px;
    color: var(--trim);
  }
  .wine-title {
    top: 282px;
    font-family: "Yellowtail", "Brush Script MT", "Segoe Script", cursive;
    font-style: normal;
    color: var(--script);
    line-height: 1;
    font-weight: 400;
  }
  .wine-title .article {
    display: block;
    font-size: 54px;
    margin-right: 30px;
  }
  .wine-title .name {
    display: block;
    font-size: 98px;
    margin-top: -10px;
  }
  .varietal {
    top: 493px;
    font-family: "Tinos", serif;
    font-size: 16px;
    color: #f2f2f2;
    letter-spacing: 0.3px;
  }
  .divider {
    position: absolute;
    left: 131px;
    top: 528px;
    width: 150px;
    height: 1px;
    background: #e8e8e8;
  }
  .winery {
    top: 548px;
    font-family: "Tinos", serif;
    font-weight: 700;
    font-size: 18px;
    color: var(--trim);
    letter-spacing: 0.4px;
  }
  .caption {
    position: absolute;
    left: 324px;
    top: 768px;
    width: 180px;
    display: flex;
    align-items: center;
    justify-content: space-between;
    font-family: "Open Sans", sans-serif;
    font-size: 19px;
    color: var(--caption);
  }
  .caption .rule {
    width: 47px;
    height: 1px;
    background: var(--caption);
  }
</style>
</head>
<body>
<main class="canvas">
  <section class="label">
    <svg class="label-shape" width="412" height="601" viewBox="0 0 412 601">
      <defs>
        <radialGradient id="grape-tone" cx="50%" cy="50%" r="55%">
          <stop offset="0%" stop-color="var(--grape-light)"/>
          <stop offset="100%" stop-color="var(--grape-dark)"/>
        </radialGradient>
      </defs>
      <path class="label-body" fill="var(--label-ink)"
        d="M70,138 A136,138 0 0 1 342,138 L381,138 A32,32 0 0 0 412,170 L412,569 A32,32 0 0 0 381,601 L31,601 A32,32 0 0 0 0,569 L0,170 A32,32 0 0 0 31,138 Z"/>
      <path class="label-trim" fill="none" stroke="var(--trim)" stroke-width="2"
        d="M80,148 A126,137 0 0 1 332,148 L374,148 A28,28 0 0 0 402,176 L402,563 A28,28 0 0 0 374,591 L38,591 A28,28 0 0 0 10,563 L10,176 A28,28 0 0 0 38,148 Z"/>
      <rect class="crest-ornament" role="img" aria-label="Ornamental scrollwork crest area"
        x="106" y="56" width="200" height="200" rx="100" fill="var(--ornament)"/>
      <rect class="grape-illustration" role="img" aria-label="Faint grape cluster and vine leaves illustration"
        x="78" y="268" width="262" height="230" rx="100" fill="url(#grape-tone)"/>
    </svg>

    <p class="label-text house-name">MIRABEL</p>

    <h1 class="label-text wine-title">
      <span class="article">The</span>
      <span class="name">Mirabel</span>
    </h1>

    <p class="label-text varietal">SAUVIGNON BLANC 2017</p>
    <div class="divider"></div>
    <p class="label-text winery">HOLLOW REED WINES</p>
  </section>

  <div class="caption">
    <span class="rule"></span>
    <span>Design</span>
    <span class="rule"></span>
  </div>
</main>
</body>
</html>
```